Copper Ridge Business Cards For New Startup

I am looking for you to design some business cards for a new startup https://copperridgehub.example. I have supplied logo, brand guidelines and our signatures as a guide.

We need this to reflect the brand guidelines and the website for brand consistency,

What is Copper Ridge?

Mallorca's Business Growth Community
Join your new business community full of passionate entrepreneurs who
love to solve problems and help each other grow together!

Any questions you can ask.

Target Market(s)

Business to Business

Contact Information for Business Card

These are attached (signatures) to the job

Font styles to use
Other font styles liked:
• Open Sans

Requirements
Must have
• Match design guidelines
Nice to have
• Photos of our faces so people remember us

```html
<!DOCTYPE html>
<html lang="en">
<head>
<meta charset="utf-8">
<title>Copper Ridge – Business Cards</title>
<link rel="stylesheet" href="https://fonts.googleapis.com/css2?family=Open+Sans:wght@400;600;700&display=swap">
<style>
  :root {
    --olive: #66692d;
    --olive-soft: #8a8d4f;
    --ink: #4a4a4a;
    --card-dark: #181818;
    --paper: #ffffff;
    --backdrop: #eeeeec;
  }
  * { margin: 0; padding: 0; box-sizing: border-box; }
  html, body { width: 1200px; height: 900px; overflow: hidden; }
  body {
    background: var(--backdrop);
    font-family: "Open Sans", Arial, sans-serif;
    position: relative;
  }

  /* Back of card */
  .card-back {
    position: absolute; left: 75px; top: 268px;
    width: 640px; height: 364px;
    background: var(--card-dark);
  }
  .card-back__pattern {
    position: absolute; inset: 0;
    background: radial-gradient(circle at 50% 50%, #222 0%, var(--card-dark) 80%);
  }
  .card-back__mark {
    position: absolute; left: 480px; top: 214px;
    width: 56px; height: 56px;
    border: 2px solid var(--olive-soft); border-radius: 50%;
  }

  /* Front of card */
  .card-front {
    position: absolute; left: 759px; top: 130px;
    width: 366px; height: 640px;
    background: var(--paper);
  }
  .brand { position: absolute; left: 41px; top: 29px; width: 300px; height: 100px; }
  .brand__mark {
    position: absolute; left: 0; top: 0;
    width: 62px; height: 56px;
    border: 3px solid var(--olive); border-radius: 50%;
  }
  .brand__name {
    position: absolute; left: 76px; top: 8px;
    font-size: 29px; font-weight: 600; color: var(--olive);
    letter-spacing: 0.5px; white-space: nowrap;
  }
  .brand__url {
    position: absolute; left: 76px; top: 46px; width: 222px;
    text-align: center; font-size: 15px; font-weight: 600; color: var(--olive);
  }
  .social { position: absolute; left: 157px; top: 98px; display: flex; gap: 14px; }
  .social__dot { width: 14px; height: 14px; border-radius: 3px; background: var(--olive); }

  .person { position: absolute; }
  .person__photo {
    width: 92px; height: 92px;
    border: 2px solid var(--olive); border-radius: 3px;
    background: linear-gradient(160deg, #d9d3c9, #8c8478);
  }
  .person__name { font-size: 17px; font-weight: 700; color: var(--olive); margin-top: 17px; white-space: nowrap; }
  .person__role { font-size: 15px; color: var(--ink); margin-top: 0; white-space: nowrap; }
  .person__contacts { list-style: none; margin-top: 9px; }
  .person__contacts li {
    display: flex; align-items: center; gap: 8px;
    font-size: 16px; color: var(--ink); line-height: 24px; white-space: nowrap;
  }
  .icon { width: 16px; height: 16px; fill: var(--olive); flex: none; }

  .person--first { left: 36px; top: 166px; }
  .person--second { right: 37px; top: 403px; text-align: right; }
  .person--second .person__photo { margin-left: auto; }
  .person--second .person__contacts li { justify-content: flex-end; }
</style>
</head>
<body>

<section class="card-back" aria-label="Card back">
  <div class="card-back__pattern" role="img" aria-label="Repeating pattern of the brand symbol in faint grey on black"></div>
  <div class="card-back__mark"></div>
</section>

<section class="card-front" aria-label="Card front">
  <div class="brand">
    <div class="brand__mark"></div>
    <div class="brand__name">COPPER RIDGE</div>
    <div class="brand__url">www.copperridgehub.example</div>
  </div>
  <div class="social" aria-label="Social profiles">
    <span class="social__dot"></span><span class="social__dot"></span><span class="social__dot"></span><span class="social__dot"></span><span class="social__dot"></span>
  </div>

  <article class="person person--first">
    <div class="person__photo" role="img" aria-label="Portrait photo of Adrian Stoke"></div>
    <h2 class="person__name">Adrian Stoke</h2>
    <p class="person__role">Founder &amp; Growth Hacker</p>
    <ul class="person__contacts">
      <li><svg class="icon" viewBox="0 0 16 16"><path d="M3.6 1 6 3.6 4.7 5.5c.9 2.2 3.2 4.7 5.8 5.8L12.4 10 15 12.4l-1.6 2.4C7.6 14.6 1.4 8.4 1.2 2.6z"/></svg>+ 34 611 482 907</li>
      <li><svg class="icon" viewBox="0 0 16 16"><path d="M1 4h14v1L8 9.5 1 5z"/><path d="M1 6.5 8 11l7-4.5V13H1z"/></svg>as@copperridgehub.example</li>
    </ul>
  </article>

  <article class="person person--second">
    <div class="person__photo" role="img" aria-label="Portrait photo of Marina Kellerman"></div>
    <h2 class="person__name">Marina Kellerman</h2>
    <p class="person__role">Relationship Director</p>
    <ul class="person__contacts">
      <li>+ 44 7700 900 415<svg class="icon" viewBox="0 0 16 16"><path d="M12.4 1 10 3.6l1.3 1.9c-.9 2.2-3.2 4.7-5.8 5.8L3.6 10 1 12.4l1.6 2.4C8.4 14.6 14.6 8.4 14.8 2.6z"/></svg></li>
      <li>mk@copperridgehub.example<svg class="icon" viewBox="0 0 16 16"><path d="M1 4h14v1L8 9.5 1 5z"/><path d="M1 6.5 8 11l7-4.5V13H1z"/></svg></li>
    </ul>
  </article>
</section>

</body>
</html>
```